Vantor Burnished Concrete & Grinding
I'm looking for a business card and logo design for my
new Polished Concrete & Grinding business,
If you were to look up Vantor in the dictionary it would
say, first in importance, order, or position; leading.
Polished Concrete floors are a niche market, that are being used currently in Shopping centres, office spaces and by most high end architects, builders and designers.
i need my business card & logo to stand out from my
competitors, i need my design + logo to reflect this it
needs to be simple, professional, eye catching, easy
to read and scream quality. The logo will need to be
suitable for a whole range of applications including,
uniforms, letter heads, stickers, and eventually
incorporating in vehicle vinyl wrapping.
Target Market(s)
Builders, architects, Interior designers & home owners
Contact Information for Business Card
Front side:
- Vantor Burnished Concrete & Grinding.
- Logo
Rear side:
- Liam Verhorst
- 0481736502
- info@vantorbcg.com.au
- commercial - domestic - industrial
- (later down the line website & space for
social media links
www.vantorburnishedconcrete.com.au)
Colors
Designer to choose colors to be used in the design.
Look and feel

```html
<!DOCTYPE html>
<html lang="en">
<head>
<meta charset="utf-8">
<title>Vantor Burnished Concrete &amp; Grinding – Business Card</title>
<link rel="stylesheet" href="https://fonts.googleapis.com/css2?family=Arimo:wght@400;700&display=swap">
<style>
  :root {
    --backdrop: #97989c;
    --card-front: #000000;
    --card-back: #e6e6e6;
    --card-edge: #b9babd;
    --accent: #f47f2f;
    --ink-light: #ffffff;
    --ink-dark: #231f20;
  }
  * { margin: 0; padding: 0; box-sizing: border-box; }
  html, body {
    width: 1200px;
    height: 997px;
    overflow: hidden;
    background: var(--backdrop);
    font-family: "Arimo", Arial, Helvetica, sans-serif;
  }
  .canvas {
    position: relative;
    width: 1200px;
    height: 997px;
  }
  .card {
    position: absolute;
    left: 231px;
    width: 738px;
    height: 410px;
    border: 1px solid var(--card-edge);
    text-align: center;
  }
  .card--front {
    top: 69px;
    background: var(--card-front);
    border-color: #3a3a3a;
  }
  .card--back {
    top: 518px;
    background: var(--card-back);
    color: var(--ink-dark);
  }
  .brand-mark {
    position: absolute;
    left: 50%;
    top: 96px;
    width: 92px;
    height: 92px;
    margin-left: -46px;
    background: var(--accent);
  }
  .brand-name {
    position: absolute;
    left: 0;
    right: 0;
    top: 232px;
    color: var(--ink-light);
    font-weight: 400;
    text-transform: uppercase;
    line-height: 1;
  }
  .brand-name__main {
    display: block;
    font-size: 29px;
    letter-spacing: 3px;
  }
  .brand-name__sub {
    display: block;
    margin-top: 12px;
    font-size: 18px;
    letter-spacing: 2.5px;
  }
  .holder-name {
    position: absolute;
    left: 0; right: 0;
    top: 44px;
    font-size: 26px;
    font-weight: 700;
  }
  .contact-list {
    position: absolute;
    left: 0; right: 0;
    top: 154px;
    list-style: none;
    font-size: 27px;
    line-height: 32px;
  }
  .website {
    position: absolute;
    left: 0; right: 0;
    top: 336px;
    font-size: 21px;
    letter-spacing: 2.4px;
  }
</style>
</head>
<body>
  <main class="canvas">
    <section class="card card--front" aria-label="Card front">
      <div class="brand-mark" aria-hidden="true"></div>
      <h1 class="brand-name">
        <span class="brand-name__main">Vantor Burnished</span>
        <span class="brand-name__sub">Concrete &amp; Grinding</span>
      </h1>
    </section>

    <section class="card card--back" aria-label="Card back">
      <h2 class="holder-name">Liam Verhorst</h2>
      <ul class="contact-list">
        <li class="contact-list__phone">0481736502</li>
        <li class="contact-list__email">info@vantorbcg.com.au</li>
        <li class="contact-list__services">commercial - domestic - industrial</li>
      </ul>
      <p class="website">www.vantorburnishedconcrete.com.au</p>
    </section>
  </main>
</body>
</html>
```